Halverin Link Group B.cards and Letterhead
B. cards
Professional
First Last
Executive
Amber Crest Tower
Office 5817
P.O.Box 6094
Jeddah 23867
Saudi Arabia
name@hlgnet.com
www.hlgnet.com
I want to print cards on pearl paper
either blank or a nice design or the logo

```html
<!DOCTYPE html>
<html lang="en">
<head>
<meta charset="utf-8">
<title>Halverin Link Group Stationery</title>
<link href="https://fonts.googleapis.com/css2?family=Exo+2:wght@400;800&family=Roboto:wght@400;500&display=swap" rel="stylesheet">
<style>
:root{
  --bg-dark:#22150c;
  --bg-mid:#3a2414;
  --glow:#c0661c;
  --blue:#1c55b4;
  --navy:#0a2566;
  --paper:#ffffff;
  --grey:#c9ced6;
  --ink:#5a6170;
  --label:#d8c9b8;
}
*{margin:0;padding:0;box-sizing:border-box}
html,body{width:1200px;height:382px;overflow:hidden}
body{
  position:relative;
  font-family:"Roboto",Arial,sans-serif;
  background:
    radial-gradient(ellipse 260px 120px at 40px 10px,rgba(192,102,28,.75),transparent 70%),
    repeating-linear-gradient(135deg,rgba(255,255,255,.025) 0 3px,transparent 3px 7px),
    linear-gradient(180deg,var(--bg-mid),var(--bg-dark));
}
.brand{position:absolute;font-family:"Exo 2",sans-serif;font-weight:800;letter-spacing:1px;line-height:1}
.brand-hero{left:42px;top:84px;font-size:54px;color:var(--paper)}
.hero-tagline{position:absolute;left:44px;top:142px;font-size:7px;color:var(--grey);letter-spacing:1px}
.label{position:absolute;font-size:6px;color:var(--label)}
.concept-label{left:44px;top:160px;font-size:8px}

.card{position:absolute;width:144px;height:77px;border-radius:2px;overflow:hidden;background:var(--paper);box-shadow:0 2px 5px rgba(0,0,0,.5)}
.card-blue{background:linear-gradient(180deg,#2b6bd0,var(--navy))}
.card .brand{font-size:26px;color:var(--blue)}
.card-blue .brand{color:var(--paper)}
.card .wave{position:absolute;left:0;bottom:0;width:100%;height:18px}
.card-info{position:absolute;left:84px;top:8px;font-size:4.5px;line-height:6px;color:var(--ink)}
.card-info strong{display:block;color:var(--navy);font-size:5.5px}

.sheet{position:absolute;top:19px;width:234px;height:318px;background:var(--paper);box-shadow:0 3px 8px rgba(0,0,0,.55);overflow:hidden}
.sheet .brand{left:18px;top:16px;font-size:24px;color:var(--blue)}
.sheet-contact{position:absolute;right:14px;top:14px;font-size:4.5px;line-height:6px;color:var(--ink)}
.sheet .wave{position:absolute;left:0;bottom:0;width:100%;height:46px}
.sheet-footer{position:absolute;left:0;right:0;bottom:6px;text-align:center;font-size:4.5px;color:var(--paper)}

.envelope{position:absolute;left:848px;width:342px;height:84px;background:var(--paper);box-shadow:0 2px 6px rgba(0,0,0,.5);overflow:hidden}
.envelope svg{position:absolute;inset:0;width:100%;height:100%}
.envelope .brand{font-size:18px;color:var(--blue)}
.env-address{position:absolute;font-size:4.5px;line-height:6px;color:var(--ink)}
</style>
</head>
<body>

<div class="brand brand-hero">HLG</div>
<div class="hero-tagline">HALVERIN LINK GROUP</div>
<div class="label concept-label">Stationery Concept</div>

<!-- Business cards -->
<div class="card" style="left:19px;top:156px">
  <div class="brand" style="left:30px;top:24px">HLG</div>
  <svg class="wave" viewBox="0 0 144 18" preserveAspectRatio="none"><path d="M0 12 Q72 2 144 8 L144 18 L0 18Z" fill="#1c55b4"/><path d="M0 10 Q72 0 144 6" stroke="#c9ced6" fill="none"/></svg>
</div>
<div class="label" style="left:19px;top:236px">Business Card Front</div>

<div class="card" style="left:175px;top:156px">
  <div class="brand" style="left:8px;top:8px;font-size:16px">HLG</div>
  <div class="card-info"><strong>First Last</strong>Executive<br>Amber Crest Tower<br>Office 5817<br>P.O.Box 6094<br>Jeddah 23867<br>name@hlgnet.com</div>
  <svg class="wave" viewBox="0 0 144 18" preserveAspectRatio="none"><path d="M0 12 Q72 2 144 8 L144 18 L0 18Z" fill="#1c55b4"/></svg>
</div>
<div class="label" style="left:175px;top:236px">Business Card Back</div>

<div class="card card-blue" style="left:19px;top:269px">
  <div class="brand" style="left:30px;top:24px">HLG</div>
</div>
<div class="label" style="left:19px;top:349px">Card Back Variant</div>

<div class="card" style="left:175px;top:269px">
  <div class="brand" style="left:8px;top:8px;font-size:16px">HLG</div>
  <div class="card-info"><strong>First Last</strong>Executive<br>Amber Crest Tower<br>Office 5817<br>Jeddah 23867<br>Saudi Arabia<br>www.hlgnet.com</div>
  <svg class="wave" viewBox="0 0 144 18" preserveAspectRatio="none"><path d="M0 10 Q72 4 144 12 L144 18 L0 18Z" fill="#0a2566"/></svg>
</div>
<div class="label" style="left:175px;top:349px">Card Front Variant</div>

<!-- Letterheads -->
<div class="sheet" style="left:338px">
  <div class="brand">HLG</div>
  <div class="sheet-contact">Amber Crest Tower<br>Office 5817<br>P.O.Box 6094<br>Jeddah 23867<br>name@hlgnet.com</div>
  <svg class="wave" viewBox="0 0 234 46" preserveAspectRatio="none"><path d="M0 26 Q117 6 234 18 L234 46 L0 46Z" fill="#1c55b4"/><path d="M0 22 Q117 2 234 14" stroke="#c9ced6" stroke-width="2" fill="none"/></svg>
  <div class="sheet-footer">www.hlgnet.com</div>
</div>
<div class="label" style="left:420px;top:342px">Letterhead A4</div>

<div class="sheet" style="left:594px">
  <div class="brand">HLG</div>
  <svg class="wave" viewBox="0 0 234 46" preserveAspectRatio="none"><path d="M0 26 Q117 6 234 18 L234 46 L0 46Z" fill="#1c55b4"/><path d="M0 22 Q117 2 234 14" stroke="#c9ced6" stroke-width="2" fill="none"/></svg>
  <div class="sheet-footer">Amber Crest Tower · Office 5817 · Jeddah 23867 · www.hlgnet.com</div>
</div>
<div class="label" style="left:676px;top:342px">Continuation Sheet</div>

<!-- Envelopes -->
<div class="envelope" style="top:19px">
  <svg viewBox="0 0 342 84" preserveAspectRatio="none"><path d="M0 0 L171 46 L342 0Z" fill="#c9ced6"/></svg>
  <div class="brand" style="left:156px;top:10px;font-size:12px;color:#fff">HLG</div>
</div>
<div class="envelope" style="top:96px">
  <svg viewBox="0 0 342 84" preserveAspectRatio="none"><path d="M0 0 L171 50 L342 0Z" fill="#1c55b4"/><path d="M0 84 L150 40 M342 84 L192 40" stroke="#e4e7ec" fill="none"/></svg>
  <div class="brand" style="left:154px;top:12px;font-size:13px;color:#fff">HLG</div>
</div>
<div class="envelope" style="top:176px">
  <svg viewBox="0 0 342 84" preserveAspectRatio="none"><path d="M0 0 L171 44 L342 0" stroke="#d9dde3" fill="none"/><path d="M0 84 L150 40 M342 84 L192 40" stroke="#e4e7ec" fill="none"/></svg>
</div>
<div class="envelope" style="top:254px">
  <div class="brand" style="left:12px;top:10px">HLG</div>
  <div class="env-address" style="left:12px;top:32px">Amber Crest Tower, Office 5817<br>P.O.Box 6094, Jeddah 23867</div>
  <svg viewBox="0 0 342 84" preserveAspectRatio="none"><path d="M0 70 Q171 58 342 66 L342 84 L0 84Z" fill="#1c55b4"/></svg>
</div>
<div class="label" style="left:990px;top:342px">DL Envelopes</div>

</body>
</html>
```